Classical Chamber Choir needs an electronic and printable flyer for an Easter Concert

I am the new Artistic Director of the Halvane Chorale. We would like to advertise our upcoming concert on April 5 and are seeking a new, more youthful, contemporary look for the choir's advertising. Previously they have used classical curly letters and dark colours. Perhaps black/grey and white would work?
The choir is 27 years old and has many loyal and some quite elderly singers. We would now like to extend our appeal to the younger singers who are in the choir - age group 35 - 60 and we are keen to attract more in the 30/40 age group. I would like something contemporary in feel, uncluttered, minimalist and artistically appealing. More Morwelt than Pilard - more Fenzarotti than Drecklin. Some inspiration starters: Valdurro line drawings, linocut designs, Emil Vortanek pencil drawings. I am hoping these references might inspire you. Here are some other ideas using line from Gyula Fenyvesi:
https://pics.vistrel.example/qw7RtPz2LmNbXcYhA
https://pics.vistrel.example/Hs3KdVn8WpJtRfZ4M
We would require an A4 flyer, (high res. and low res.) DL, jpg for Chatterly and a 10cm. size to put on the front of the Concert Programme.

```html
<!DOCTYPE html>
<html lang="en">
<head>
<meta charset="utf-8">
<title>Holbrant at Easter — Halvane Chorale</title>
<link rel="stylesheet" href="https://fonts.googleapis.com/css2?family=Cormorant+Garamond:wght@400;500;600&display=swap">
<style>
  :root {
    --backdrop: #2c2c2c;
    --paper: #f4f4f2;
    --ink: #2a2f33;
    --ink-soft: #3a3f43;
    --tone-dark: #1f2529;
    --tone-mid: #8a8f8e;
    --tone-light: #e6e6df;
  }
  * { margin: 0; padding: 0; box-sizing: border-box; }
  html, body {
    width: 1200px; height: 1200px; overflow: hidden;
    background: var(--backdrop);
  }
  .canvas { position: relative; width: 1200px; height: 1200px; }
  .flyer {
    position: absolute; left: 190px; top: 20px;
    width: 982px; height: 1390px;
    background: var(--paper);
    transform: scale(0.8345);
    transform-origin: 0 0;
    font-family: "Cormorant Garamond", "Times New Roman", serif;
    color: var(--ink);
  }
  .artwork { position: absolute; left: 0; top: 0; width: 982px; height: 1390px; }
  .presenter {
    position: absolute; top: 90px; left: 0; width: 100%;
    text-align: center; font-size: 24px; font-weight: 500;
    letter-spacing: 0.28em; text-transform: uppercase;
  }
  .title {
    position: absolute; top: 128px; left: 0; width: 100%;
    text-align: center; font-size: 80px; font-weight: 400;
    letter-spacing: 0.01em; line-height: 1;
  }
  .programme {
    position: absolute; top: 260px; right: 66px;
    text-align: right; font-size: 19px; line-height: 24.5px;
    color: var(--ink-soft);
  }
  .programme strong { font-weight: 600; color: var(--ink); }
  .programme .venue { margin-top: 13px; }
  .credits { position: absolute; font-size: 20px; line-height: 26px; color: var(--ink-soft); }
  .credits h3 {
    font-size: 22px; font-weight: 600; color: var(--ink);
    letter-spacing: 0.02em; line-height: 26px;
  }
  .credits .group { margin-bottom: 27px; }
  .credits--left { left: 78px; top: 1034px; }
  .credits--left .group--ensemble { margin-bottom: 30px; }
  .credits--right { right: 66px; top: 1034px; text-align: right; }
  .credits--right .group { margin-bottom: 30px; }
  .tickets {
    position: absolute; top: 1282px; left: 0; width: 100%;
    text-align: center; font-size: 21px; line-height: 28px; color: var(--ink-soft);
  }
</style>
</head>
<body>
<main class="canvas">
  <article class="flyer">
    <svg class="artwork" viewBox="0 0 982 1390" role="img" aria-label="Monochrome photograph of a slender figure in flowing layered fabric standing in windswept grass under a misty sky, framed by a torn brush-stroke edge">
      <defs>
        <linearGradient id="mistTone" x1="0" y1="0" x2="1" y2="0.35">
          <stop offset="0" stop-color="var(--tone-dark)"/>
          <stop offset="0.3" stop-color="#5b6266"/>
          <stop offset="0.55" stop-color="var(--tone-light)"/>
          <stop offset="0.82" stop-color="#cfd0ca"/>
          <stop offset="1" stop-color="#5f6669"/>
        </linearGradient>
        <radialGradient id="mistGlow" cx="0.62" cy="0.55" r="0.45">
          <stop offset="0" stop-color="#f0f0ea" stop-opacity="0.9"/>
          <stop offset="1" stop-color="#f0f0ea" stop-opacity="0"/>
        </radialGradient>
        <linearGradient id="groundTone" x1="0" y1="0" x2="0" y2="1">
          <stop offset="0.7" stop-color="#000" stop-opacity="0"/>
          <stop offset="1" stop-color="#3c4245" stop-opacity="0.55"/>
        </linearGradient>
        <path id="brushField" d="M0,262 L18,258 L30,266 L52,262 L70,270 L96,266 L120,276 L150,280 L190,294 L230,306 L280,326 L330,350 L380,374 L430,398 L480,428 L530,456 L580,484 L630,510 L680,528 L720,540 L760,538 L800,522 L840,500 L880,480 L920,462 L950,444 L962,430 L975,420 L982,398 L982,880 L968,884 L955,878 L940,896 L910,900 L880,918 L850,930 L820,946 L800,966 L780,990 L770,1004 L760,990 L740,972 L700,962 L660,966 L620,954 L580,960 L540,966 L500,962 L460,970 L420,958 L380,962 L340,950 L300,952 L260,944 L220,936 L180,948 L140,962 L110,956 L80,972 L55,962 L30,948 L12,946 L0,936 Z"/>
      </defs>
      <use href="#brushField" fill="url(#mistTone)"/>
      <use href="#brushField" fill="url(#mistGlow)"/>
      <use href="#brushField" fill="url(#groundTone)"/>
    </svg>

    <p class="presenter">Halvane Chorale present</p>
    <h1 class="title">HOLBRANT AT EASTER</h1>

    <section class="programme">
      <p><strong>HOLBRANT VESPER CANTICLE H 318</strong></p>
      <p>in the company of the <strong>RUSSIAN MASTERS</strong></p>
      <p>Varlenov, Glazkin, Ramotinsky, Borevsk</p>
      <p class="venue"><strong>ST ALDRIC CHAPEL CHURCH</strong></p>
      <p>Orlen Street Brackwood Hill</p>
      <p>5PM April 5 2020</p>
    </section>

    <section class="credits credits--left">
      <div class="group">
        <h3>SOLOISTS</h3>
        <p>Mira Talbrook, Anton Weylridge, Gareth Colwyn</p>
      </div>
      <div class="group group--ensemble">
        <h3>MEN IN CHORD</h3>
      </div>
      <div class="group">
        <h3>STRING QUARTET</h3>
        <p>Ilya Vessarin, Maren Lio, Rowan Hesket, Zsolt Varenyi</p>
      </div>
    </section>

    <section class="credits credits--right">
      <div class="group">
        <h3>ORGAN</h3>
        <p>Josette Arlin</p>
      </div>
      <div class="group">
        <h3>ARTISTIC DIRECTOR</h3>
        <p>Edit Maravolgyi</p>
      </div>
    </section>

    <footer class="tickets">
      <p>Tickets $30/ $25/ $10 Student/ Children under 12 free</p>
      <p>Programmes: Gold Coin Donation</p>
    </footer>
  </article>
</main>
</body>
</html>
```